Business Card design for Brightvale Global

we need a business card design for our company. we are a trading company based in LA.

Company Name: Brightvale Global Corp.
Contact: Marcus Ortega
Title: CEO
Tel: 310-647-2093
Email: bvgcorp7@mailnest.example

Target Market(s)

International, especially China

Industry/Entity Type

Trade

Colors
3276b5
34a7d8
0555a3
0493ce
85cae6
85acd3
d0dfed
cee9f5

Requirements
Must have
• Logo and contact, to have international/global feeling

```html
<!DOCTYPE html>
<html lang="en">
<head>
<meta charset="utf-8">
<title>Brightvale Global – Business Card</title>
<link rel="stylesheet" href="https://fonts.googleapis.com/css2?family=Lato:wght@400;700&display=swap">
<style>
  :root {
    --stage: #161617;
    --card: #2a2a2c;
    --card-edge: #232325;
    --accent: #2f8fd8;
    --accent-light: #34a7d8;
    --ink: #f2f2f2;
    --silver: #b9bbbe;
    --muted: #8e9094;
  }
  * { box-sizing: border-box; margin: 0; padding: 0; }
  html, body {
    width: 1200px; height: 900px; overflow: hidden;
    background: var(--stage);
    font-family: "Lato", sans-serif;
  }
  .canvas {
    width: 1200px; height: 900px;
    display: flex; flex-direction: column; align-items: center; justify-content: center;
    gap: 40px;
  }
  .card {
    position: relative;
    width: 700px; height: 400px;
    background: linear-gradient(135deg, var(--card-edge), var(--card) 60%, #323234);
    border-bottom: 7px solid var(--accent);
    overflow: hidden;
  }
  /* Back side */
  .card-back {
    display: flex; flex-direction: column; align-items: center; justify-content: center;
  }
  .wordmark {
    display: flex; align-items: center; gap: 16px;
  }
  .wordmark-dot {
    width: 58px; height: 58px; border-radius: 50%;
  }
  .wordmark-name {
    font-weight: 700; letter-spacing: 0.5px;
  }
  .card-back .wordmark-dot { background: #3a3b3e; }
  .card-back .wordmark-name { font-size: 56px; color: var(--silver); }
  .website {
    margin-top: 70px;
    font-size: 19px; letter-spacing: 2px; color: var(--ink);
  }
  .website .domain { color: var(--accent-light); }

  /* Front side */
  .card-front {
    display: flex; align-items: center;
    padding: 0 50px 0 46px;
  }
  .card-front .wordmark { gap: 12px; width: 310px; }
  .card-front .wordmark-dot { width: 42px; height: 42px; background: var(--accent); }
  .card-front .wordmark-name { font-size: 34px; color: var(--accent); }
  .divider {
    width: 3px; height: 135px; background: var(--accent);
    margin: 0 30px 0 10px;
  }
  .person-name {
    font-size: 28px; font-weight: 700; letter-spacing: 1.5px;
    color: var(--accent); text-transform: uppercase;
  }
  .person-title { font-size: 20px; color: var(--ink); margin-bottom: 18px; }
  .contact-list { list-style: none; }
  .contact-item {
    display: flex; align-items: center; gap: 12px;
    font-size: 19px; color: var(--ink); letter-spacing: 0.5px;
    line-height: 1.5;
  }
  .contact-icon { width: 16px; height: 16px; flex: none; }
</style>
</head>
<body>
<main class="canvas">
  <section class="card card-back" aria-label="Card back">
    <div class="wordmark">
      <span class="wordmark-dot"></span>
      <span class="wordmark-name">Brightvale Global</span>
    </div>
    <p class="website">www.<span class="domain">brightvaleglobal</span>.example</p>
  </section>

  <section class="card card-front" aria-label="Card front">
    <div class="wordmark">
      <span class="wordmark-dot"></span>
      <span class="wordmark-name">Brightvale Global</span>
    </div>
    <div class="divider"></div>
    <div class="person">
      <h1 class="person-name">Marcus Ortega</h1>
      <p class="person-title">CEO</p>
      <ul class="contact-list">
        <li class="contact-item">
          <svg class="contact-icon" viewBox="0 0 16 16"><path fill="#2f8fd8" d="M3.5 1 6 3.6 4.7 5.4c.8 1.9 2.1 3.2 4 4l1.8-1.3L15 10.5l-1.6 3.1C7.4 13.8 2.2 8.6 2.4 2.6z"/></svg>
          310-647-2093
        </li>
        <li class="contact-item">
          <svg class="contact-icon" viewBox="0 0 16 16"><rect x="1" y="3" width="14" height="10" fill="#2f8fd8"/><path d="M1 3.5 8 9l7-5.5" fill="none" stroke="#2a2a2c" stroke-width="1.4"/></svg>
          bvgcorp7@mailnest.example
        </li>
        <li class="contact-item">
          <svg class="contact-icon" viewBox="0 0 16 16" fill="none" stroke="#2f8fd8" stroke-width="1.3"><circle cx="8" cy="8" r="6.5"/><ellipse cx="8" cy="8" rx="3" ry="6.5"/><path d="M1.5 8h13M2.5 4.7h11M2.5 11.3h11"/></svg>
          brightvaleglobal.example
        </li>
      </ul>
    </div>
  </section>
</main>
</body>
</html>
```